Namecard Designs+Logo for a High End Automobile Company

We need a new business card for our company called Velta Motorhof.

www.veltamotorhof.example.sg
Our new website will be up in 2.5 months time.

We sell used and brand new continental cars like Korvane, QTL, Dravell, Solbrini and etc. Currently we are operating from 2 offices in Singapore and United Kingdom.

We want a design which is serious. We are open to colours but try to keep it at a maximum of 3 colours.

We prefer something simple and minimal. We are open to 2 sides printing or even 2 sided namecards. Both UK and Singapore company offices address must be in; either side by side, front and back, or even 2 sided cards.

The logo can be a text logo, emblem, abstract, pictorial or combination.

We are printing with Pribo.com so please kindly follow the printing guideline.

http://uk.pribo.example/help/faq/templates-and-guidelines.html

Rich and Car Enthusiasts

Printing

Must have
• Our 2 offices; UK and Singapore.

Our slogan which is " The Automobile Specialist"
Should not have
• Not more than 3 colours

```html
<!DOCTYPE html>
<html lang="en">
<head>
<meta charset="utf-8">
<title>Velta Motorhof — Business Card</title>
<link rel="stylesheet" href="https://fonts.googleapis.com/css2?family=Orbitron:wght@500&family=Share+Tech&display=swap">
<style>
  :root {
    --page: #ffffff;
    --card: #000000;
    --card-edge: #3a3a3a;
    --wordmark: #8f8f8f;
    --slogan: #d4d4d4;
    --detail: #e2e2e2;
  }
  * { margin: 0; padding: 0; box-sizing: border-box; }
  html, body {
    width: 1200px;
    height: 394px;
    overflow: hidden;
    background: var(--page);
  }
  .card {
    position: relative;
    width: 1200px;
    height: 394px;
    background: var(--card);
    border: 1px solid var(--card-edge);
    border-radius: 60px 0 60px 0;
    overflow: hidden;
  }
  .brand {
    position: absolute;
    left: 0;
    right: 0;
    top: 158px;
    text-align: center;
  }
  .brand__name {
    font-family: "Orbitron", sans-serif;
    font-weight: 500;
    font-size: 38px;
    letter-spacing: 2px;
    color: var(--wordmark);
    line-height: 1;
  }
  .brand__slogan {
    margin-top: 18px;
    font-family: "Orbitron", sans-serif;
    font-weight: 500;
    font-size: 9px;
    letter-spacing: 6.5px;
    color: var(--slogan);
    text-transform: uppercase;
  }
  .office {
    position: absolute;
    top: 292px;
    width: 340px;
    text-align: center;
    font-family: "Share Tech", sans-serif;
    font-size: 11px;
    letter-spacing: 1.2px;
    line-height: 15px;
    color: var(--detail);
    text-transform: uppercase;
  }
  .office--singapore { left: 58px; }
  .office--uk { left: 824px; }
  .office__country { margin-bottom: 15px; }
</style>
</head>
<body>
  <main class="card">
    <div class="brand">
      <h1 class="brand__name">VELTA MOTORHOF</h1>
      <p class="brand__slogan">The Automobile Specialist</p>
    </div>

    <address class="office office--singapore">
      <p class="office__country">Singapore</p>
      <p>8 Harbourline Road, Quay House, #02-01,</p>
      <p>Singapore 048111</p>
    </address>

    <address class="office office--uk">
      <p class="office__country">United Kingdom</p>
      <p>8 Harbourline Road, Quay House, #02-01,</p>
      <p>Singapore 048111</p>
    </address>
  </main>
</body>
</html>
```